Web site for Copper Lantern Cleaner and Protectant

We need a website for a new company called Copper Lantern, LLC. We make and resell a simple spray and wipe waterless all purpose cleaner a protectant safe on all surfaces for use on RVs, boats, cars and motorcycles. This is an eco-friendly green product.

The website will be our store front with product info, training videos, events, social media feeds, and link to our markets space for purchases. We will be working to establish distributers and resellers and as such will be traveling to RV and car shows heavily the first couple of years.

It cleans and protects in a simple spray and wipe step leaving the surface protected and conditioned to repel dust, dirt, water, smudges, bugs and fingerprints while preventing fogging. Safe on acrylic, clarivex, durimon, plastic, rubber, painted surfaces, chrome, stainless, aluminum, vinyl, leather, glass.... This is an eco-friendly green product.

We want to play off the company name to tell the consumer that the product is easy to use and associate to the nostalgics 1950's in the USA.

Attached is our Logo and draft of the labels we will be using for the products. Please let me know what other information you need to get started.

Thank you

```html
<!DOCTYPE html>
<html lang="en">
<head>
<meta charset="utf-8">
<title>Copper Lantern, LLC</title>
<link href="https://fonts.googleapis.com/css2?family=Open+Sans:wght@400;600;700&family=Noto+Serif:wght@400&display=swap" rel="stylesheet">
<style>
:root{
  --blue:#0a8fd6;
  --blue-dark:#0577b8;
  --blue-light:#2aa3e6;
  --ink:#444;
  --grey:#666;
  --footer:#2f2f2f;
  --footer-text:#9a9a9a;
  --white:#fff;
}
*{margin:0;padding:0;box-sizing:border-box}
html,body{width:1000px;height:1200px;overflow:hidden}
body{position:relative;font-family:"Open Sans",sans-serif;background:var(--white);color:var(--ink)}
.abs{position:absolute}
.line{display:block;white-space:nowrap}

.brand{position:absolute;left:86px;top:30px;height:34px;display:flex;align-items:center;gap:9px;z-index:3}
.brand-mark{width:30px;height:30px;border-radius:50%;background:var(--blue);flex-shrink:0}
.brand-name{font-size:19px;font-weight:700;color:var(--blue);white-space:nowrap;line-height:1}

.contact-top{left:296px;top:27px;font-size:14px;color:var(--grey)}
.contact-top div{display:flex;align-items:center;gap:8px;height:23px}
.contact-top .phone{font-weight:700}
.search{left:654px;top:33px;width:264px;height:28px;border:1px solid #444;display:flex}
.search span{flex:1;font-size:9px;color:#666;padding:8px 6px}
.search b{width:28px;background:var(--blue);display:flex;align-items:center;justify-content:center}

.nav-bar{left:0;top:94px;width:1000px;height:43px;background:linear-gradient(var(--blue-light),var(--blue))}
.nav{left:296px;top:94px;height:43px;display:flex}
.nav a{color:var(--white);font-size:11.5px;font-weight:600;text-decoration:none;padding:0 13px;line-height:43px}
.nav a.current{background:var(--blue-dark);padding:0 15px}
.social{display:flex;gap:20px}
.social i{width:16px;height:16px;transform:rotate(45deg);display:block;background:var(--blue-dark)}
.social-top{left:826px;top:107px}

.hero{left:0;top:137px;width:1000px;height:321px;background:linear-gradient(100deg,#6b6157 0%,#a8332a 25%,#c73a2e 45%,#7a2a25 65%,#8c8a86 85%,#b5b2ac 100%)}
.arrow{top:286px}

h2{font-weight:400;color:var(--blue);font-size:19px}
.shop-title{left:81px;top:491px}
.shop-sub{left:82px;top:524px;font-size:12.5px;font-weight:600;color:#444}
.shop-text{left:82px;top:549px;font-size:10px;letter-spacing:-0.1px;line-height:14.4px;color:#777}
.btn{display:block;border-radius:4px;font-size:10.5px;text-align:center;text-decoration:none}
.shop-btn{left:82px;top:626px;width:71px;height:28px;line-height:26px;border:1px solid var(--blue);color:var(--blue)}
.product-img{left:382px;top:528px;width:230px;height:200px;background:linear-gradient(#f4f5f6,#dcdfe2);border-radius:6px}
.video-title{left:653px;top:487px}
.video{left:654px;top:528px;width:262px;height:153px;background:linear-gradient(120deg,#7b7b7b,#3d3a37 55%,#2a6fc9 75%,#555)}
.play{left:768px;top:593px;width:36px;height:26px;border-radius:6px;background:rgba(255,255,255,.85)}

.band{left:0;top:772px;width:1000px;height:285px}
.welcome-pre{left:83px;top:803px;font-size:16px;color:var(--white)}
.welcome-title{left:83px;top:822px;font-size:20.5px;font-weight:700;color:var(--white)}
.welcome-text{left:82px;top:853px;font-size:8px;letter-spacing:-0.15px;line-height:12.9px;font-weight:600;color:var(--white)}
.read-btn{left:83px;top:974px;width:70px;height:27px;line-height:27px;background:var(--white);color:var(--blue)}

.events-title{left:656px;top:795px;font-size:17px}
.events-intro{left:656px;top:826px;font-size:8.5px;line-height:12.8px;color:#555}
.event{left:654px;width:267px;height:57px;display:flex;gap:14px;border-bottom:1px solid #ccc;padding-top:6px}
.event:last-child{border:none}
.event svg{flex-shrink:0;margin-top:2px}
.event h3{font-size:10px;font-weight:600;color:var(--blue);margin-bottom:1px;white-space:nowrap}
.event p{font-family:"Noto Serif",serif;font-size:8.2px;line-height:12.8px;color:#555}

.footer{left:0;top:1057px;width:1000px;height:143px;background:var(--footer)}
.foot-brand{left:84px;top:1115px;height:26px;display:flex;align-items:center;gap:7px}
.foot-brand .brand-mark{width:20px;height:20px}
.foot-brand .brand-name{font-size:14px}
.foot-contact{left:225px;top:1090px;font-size:9px;color:var(--footer-text)}
.foot-contact div{display:flex;gap:8px;margin-bottom:8px;line-height:12px}
.foot-contact .addr{font-size:10px}
.social-foot{left:826px;top:1101px}
.social-foot i{background:#555}
.social-foot i:first-child{background:#3a5fb0}
.foot-nav{left:561px;top:1133px;width:357px;display:flex;justify-content:space-between}
.foot-nav a{color:var(--footer-text);font-size:10.6px;text-decoration:none}
.foot-rule{left:561px;top:1169px;width:357px;height:1px;background:#555}
.copyright{left:561px;top:1176px;width:357px;text-align:right;font-size:8.5px;color:var(--footer-text)}
</style>
</head>
<body>

<div class="brand"><span class="brand-mark"></span><span class="brand-name">Copper Lantern</span></div>

<div class="abs contact-top">
  <div><svg width="12" height="10" viewBox="0 0 12 10"><rect width="12" height="10" fill="#777"/><path d="M0 0l6 5 6-5" stroke="#fff" fill="none"/></svg>hello@copperlanterncare.com</div>
  <div class="phone"><svg width="12" height="12" viewBox="0 0 12 12"><path d="M2 0l3 3-1.5 2a7 7 0 003.5 3.5L9 7l3 3-2 2C5 12 0 7 0 2z" fill="#777"/></svg>(555)010 4827</div>
</div>

<div class="abs search"><span>Search here...</span><b><svg width="12" height="12" viewBox="0 0 12 12"><circle cx="5" cy="5" r="3.6" stroke="#fff" stroke-width="1.8" fill="none"/><path d="M7.6 7.6L11 11" stroke="#fff" stroke-width="2"/></svg></b></div>

<div class="abs nav-bar"></div>
<nav class="abs nav">
  <a class="current" href="#">Home</a><a href="#">About Us</a><a href="#">Products</a><a href="#">Services</a><a href="#">Bolg</a><a href="#">Contact</a>
</nav>
<div class="abs social social-top"><i></i><i></i><i></i></div>

<div class="abs hero" role="img" aria-label="Red sports coupe driving through an underpass"></div>
<svg class="abs arrow" style="left:70px" width="14" height="22" viewBox="0 0 14 22"><path d="M12 2L3 11l9 9" stroke="#fff" stroke-width="2.5" fill="none"/></svg>
<svg class="abs arrow" style="left:917px" width="14" height="22" viewBox="0 0 14 22"><path d="M2 2l9 9-9 9" stroke="#fff" stroke-width="2.5" fill="none"/></svg>

<h2 class="abs shop-title">Shop Our Products</h2>
<div class="abs shop-sub">Waterless All Purpose Cleaner &amp; Protectant</div>
<p class="abs shop-text">
  <span class="line">Lorem Ipsum is simply dummy text of the printing and type-</span>
  <span class="line">setting industry. Lorem Ipsum has been the industry's stan-</span>
  <span class="line">dard dummy text ever since the 1500s, when an unknown</span>
  <span class="line">printer took a galley of type .</span>
</p>
<a class="abs btn shop-btn" href="#">Shop Now</a>
<div class="abs product-img" role="img" aria-label="Spray bottle, jug and canister of Copper Lantern cleaner"></div>

<h2 class="abs video-title">Training Videos</h2>
<div class="abs video" role="img" aria-label="Training video still: wiping a car dashboard with a blue cloth"></div>
<svg class="abs play" viewBox="0 0 36 26"><path d="M14 7l10 6-10 6z" fill="#888"/></svg>

<svg class="abs band" viewBox="0 0 1000 285" preserveAspectRatio="none">
  <rect width="1000" height="285" fill="#0a8fd6"/>
  <path d="M626 0H1000V285H626L494 150a12 12 0 010-15z" fill="#fff"/>
  <path d="M617 0L484 134a12 12 0 000 17l133 134" stroke="#fff" stroke-width="3" fill="none"/>
  <rect x="626" y="0" width="374" height="4" fill="#0a8fd6"/>
  <rect x="626" y="281" width="374" height="4" fill="#0a8fd6"/>
</svg>

<div class="abs welcome-pre">Welcome to</div>
<div class="abs welcome-title">Copper Lantern LLC.</div>
<p class="abs welcome-text">
  <span class="line">Lorem Ipsum is simply dummy text of the printing and typesetting industry.</span>
  <span class="line">Lorem Ipsum has been the industry's standard dummy text ever since the 1500s,</span>
  <span class="line">when an unknown printer took a galley of type and scrambled it to make a type</span>
  <span class="line">specimen book. It has survived not only five centuries, but also the leap into</span>
  <span class="line">electronic typesetting, remaining essentially unchanged. It was popularised in the</span>
  <span class="line">1960s with the release of Typeforge sheets containing Lorem Ipsum passages, and</span>
  <span class="line">more recently with desktop publishing software like Quillset Layout including</span>
  <span class="line">versions of Lorem Ipsum.</span>
</p>
<a class="abs btn read-btn" href="#">Read More</a>

<h2 class="abs events-title">Events/News</h2>
<p class="abs events-intro">
  <span class="line">Lorem Ipsum is simply dummy text of the printing and typeset-</span>
  <span class="line">ting industry. Lorem Ipsum has been the industry's.</span>
</p>
<div class="abs event" style="top:868px">
  <svg width="23" height="24" viewBox="0 0 23 24"><rect x="1" y="3" width="21" height="20" fill="none" stroke="#0a8fd6" stroke-width="2"/><rect x="1" y="3" width="21" height="5" fill="#0a8fd6"/><path d="M6 0v5M17 0v5M5 12h13M5 16h13M5 20h13M9 9v13M14 9v13" stroke="#0a8fd6" stroke-width="1.6"/></svg>
  <div><h3>LOREM IPSUM IS SIMPLY DUMMY</h3><p>Lorem Ipsum is simply dummy text of the printing and typesetting industry. Lorem Ipsum has been</p></div>
</div>
<div class="abs event" style="top:925px">
  <svg width="23" height="24" viewBox="0 0 23 24"><rect x="1" y="3" width="21" height="20" fill="none" stroke="#0a8fd6" stroke-width="2"/><rect x="1" y="3" width="21" height="5" fill="#0a8fd6"/><path d="M6 0v5M17 0v5M5 12h13M5 16h13M5 20h13M9 9v13M14 9v13" stroke="#0a8fd6" stroke-width="1.6"/></svg>
  <div><h3>LOREM IPSUM IS SIMPLY DUMMY</h3><p>Lorem Ipsum is simply dummy text of the printing and typesetting industry. Lorem Ipsum has been</p></div>
</div>
<div class="abs event" style="top:982px">
  <svg width="23" height="24" viewBox="0 0 23 24"><rect x="1" y="3" width="21" height="20" fill="none" stroke="#0a8fd6" stroke-width="2"/><rect x="1" y="3" width="21" height="5" fill="#0a8fd6"/><path d="M6 0v5M17 0v5M5 12h13M5 16h13M5 20h13M9 9v13M14 9v13" stroke="#0a8fd6" stroke-width="1.6"/></svg>
  <div><h3>LOREM IPSUM IS SIMPLY DUMMY</h3><p>Lorem Ipsum is simply dummy text of the printing and typesetting industry. Lorem Ipsum has been</p></div>
</div>

<footer class="abs footer"></footer>
<div class="abs foot-brand"><span class="brand-mark"></span><span class="brand-name">Copper Lantern</span></div>
<div class="abs foot-contact">
  <div><svg width="10" height="8" viewBox="0 0 12 10"><rect width="12" height="10" fill="#777"/><path d="M0 0l6 5 6-5" stroke="#2f2f2f" fill="none"/></svg>hello@copperlanterncare.com</div>
  <div><svg width="10" height="10" viewBox="0 0 12 12"><path d="M2 0l3 3-1.5 2a7 7 0 003.5 3.5L9 7l3 3-2 2C5 12 0 7 0 2z" fill="#777"/></svg>(555)010 4827</div>
  <div class="addr"><svg width="8" height="11" viewBox="0 0 8 11"><path d="M4 11S0 6 0 4a4 4 0 018 0c0 2-4 7-4 7z" fill="#777"/><circle cx="4" cy="4" r="1.5" fill="#2f2f2f"/></svg><span>1420 Elmwood Lane<br>Fairhaven, KS 66010</span></div>
</div>
<div class="abs social social-foot"><i></i><i></i><i></i></div>
<nav class="abs foot-nav"><a href="#">Home</a><a href="#">About Us</a><a href="#">Products</a><a href="#">Services</a><a href="#">Bolg</a><a href="#">Contact</a></nav>
<div class="abs foot-rule"></div>
<div class="abs copyright">Copyright © 2015 Copper Lantern LLC. All Rights Reserved.</div>

</body>
</html>
```